Ribbon Works - One sheet needed for Sales Team

We need a One Sheet that introduces our business and what we do to prospective customers. This will be used both digitally and print for sales calls, both virtually and in person. Ideally we'd like this to match our branding and messaging from our website ribbonworksgrp.com so there is consistency with our messaging. Also, we have a desire for this to have a call to action that directs to our website and main phone where we have lead capture ability.
It should be clean and consistent with current marketing trends. We would like to include information about the business, our value proposition of being able to save customers up to 60% off their copy and printing costs, and some differentiators (i.e. 80+ point inspection of equipment, full teardown and rebuild of like new units, transparent pricing and lease options, 6 month warranty, comprehensive maintenance programs).

```html
<!DOCTYPE html>
<html lang="en">
<head>
<meta charset="utf-8">
<title>Ribbon Works – Sales One Sheet</title>
<link rel="stylesheet" href="https://fonts.googleapis.com/css2?family=Bebas+Neue&family=Source+Sans+3:wght@400;600&display=swap">
<style>
  :root {
    --charcoal: #1d1d1f;
    --charcoal-soft: #2b2b2e;
    --teal: #1aa3c4;
    --teal-deep: #0e8fb0;
    --paper: #f2f2f3;
    --white: #ffffff;
    --ink: #1b1b1b;
    --magenta: #e3287d;
    --yellow: #f4d21b;
    --green: #5cc34a;
    --page: #e6e6e6;
  }
  html, body {
    margin: 0;
    padding: 0;
    width: 1030px;
    height: 1200px;
    overflow: hidden;
    background: var(--page);
  }
  .sheet {
    position: relative;
    width: 1030px;
    height: 1200px;
    overflow: hidden;
    background: var(--charcoal);
    font-family: "Source Sans 3", Arial, sans-serif;
  }
  .sheet-backdrop {
    position: absolute;
    inset: 0;
  }
  .brand-name {
    position: absolute;
    left: 62px;
    top: 92px;
    margin: 0;
    font-family: "Bebas Neue", Impact, sans-serif;
    font-weight: 400;
    font-size: 84px;
    line-height: 1;
    letter-spacing: 1px;
    color: var(--ink);
  }
  .intro {
    position: absolute;
    left: 470px;
    top: 478px;
    width: 530px;
    text-align: right;
  }
  .intro-title {
    margin: 0 0 12px;
    font-family: "Bebas Neue", Impact, sans-serif;
    font-weight: 400;
    font-size: 31px;
    letter-spacing: 0.3px;
    color: var(--teal);
    line-height: 1;
  }
  .intro-text {
    margin: 0;
    font-size: 16.5px;
    line-height: 1.32;
    color: var(--white);
  }
  .offer {
    position: absolute;
    left: 484px;
    top: 738px;
  }
  .offer-headline {
    margin: 0;
    font-family: "Bebas Neue", Impact, sans-serif;
    font-weight: 400;
    font-size: 66px;
    line-height: 1;
    color: var(--teal);
  }
  .offer-headline .offer-off { font-size: 46px; }
  .offer-sub {
    margin: 4px 0 0;
    font-family: "Bebas Neue", Impact, sans-serif;
    font-weight: 400;
    font-size: 38px;
    line-height: 1;
    color: var(--teal);
  }
  .benefits {
    position: absolute;
    left: 484px;
    top: 866px;
    margin: 0;
    padding: 0;
    list-style: none;
  }
  .benefit {
    display: flex;
    align-items: center;
    gap: 12px;
    height: 40px;
    font-size: 23px;
    font-weight: 600;
    color: var(--ink);
  }
  .benefit svg { width: 19px; height: 19px; flex: none; }
  .badge {
    position: absolute;
    left: 56px;
    top: 916px;
    width: 200px;
    height: 200px;
    border-radius: 50%;
    background: var(--teal);
    box-shadow: 0 0 0 8px rgba(255,255,255,0.75);
    display: flex;
    align-items: center;
    justify-content: center;
    text-align: center;
    font-family: "Bebas Neue", Impact, sans-serif;
    font-size: 27px;
    line-height: 1.25;
    color: var(--white);
  }
  .footer-contacts {
    position: absolute;
    left: 44px;
    top: 1138px;
    height: 62px;
    display: flex;
    align-items: center;
    gap: 30px;
    font-size: 19px;
    color: var(--white);
  }
  .contact { display: flex; align-items: center; gap: 10px; }
  .contact svg { width: 26px; height: 26px; }
  .cta {
    position: absolute;
    left: 600px;
    top: 1122px;
    height: 78px;
    display: flex;
    align-items: center;
    gap: 14px;
    font-family: "Bebas Neue", Impact, sans-serif;
    font-size: 36px;
    color: var(--white);
  }
  .cta-phone { display: flex; align-items: center; gap: 10px; font-size: 33px; }
  .cta-phone svg { width: 22px; height: 28px; }
</style>
</head>
<body>
<main class="sheet">
  <svg class="sheet-backdrop" width="1030" height="1200" viewBox="0 0 1030 1200" aria-hidden="false">
    <defs>
      <linearGradient id="spectrum" x1="0" x2="1" y1="0" y2="0">
        <stop offset="0" stop-color="#e3287d" stop-opacity="0"/>
        <stop offset="0.35" stop-color="#f4d21b"/>
        <stop offset="0.6" stop-color="#5cc34a"/>
        <stop offset="0.85" stop-color="#8a4bbf"/>
        <stop offset="1" stop-color="#e3287d"/>
      </linearGradient>
      <linearGradient id="teamPhoto" x1="0" x2="1" y1="0" y2="0">
        <stop offset="0" stop-color="#ffffff"/>
        <stop offset="0.25" stop-color="#e9e7e4"/>
        <stop offset="0.6" stop-color="#b9b5b0"/>
        <stop offset="1" stop-color="#8f8c89"/>
      </linearGradient>
      <linearGradient id="copierPhoto" x1="0" x2="1" y1="0" y2="0">
        <stop offset="0" stop-color="#3a3a3d"/>
        <stop offset="0.6" stop-color="#2a2a2c"/>
        <stop offset="0.65" stop-color="#e8e8e8"/>
        <stop offset="1" stop-color="#d4d4d4"/>
      </linearGradient>
      <radialGradient id="splash" cx="0.5" cy="0.5" r="0.5">
        <stop offset="0" stop-color="#f4d21b" stop-opacity="0.55"/>
        <stop offset="0.5" stop-color="#e3287d" stop-opacity="0.35"/>
        <stop offset="1" stop-color="#5cc34a" stop-opacity="0"/>
      </radialGradient>
    </defs>

    <!-- lower light panel -->
    <path class="panel-light" d="M0 770 C 220 700 520 618 760 640 C 900 652 990 690 1030 712 V1200 H0 Z" fill="var(--paper)"/>
    <path class="panel-edge" d="M300 690 C 520 618 760 628 1030 712" fill="none" stroke="url(#spectrum)" stroke-width="6"/>
    <ellipse class="panel-splash" cx="150" cy="900" rx="190" ry="170" fill="url(#splash)"/>

    <!-- top header panel -->
    <path class="panel-header" d="M60 0 H1030 V392 C 780 448 470 430 290 350 C 160 290 70 200 0 150 V0 Z" fill="var(--white)"/>
    <path role="img" aria-label="Photo of a business team reviewing printed charts around a table"
          d="M340 0 H1030 V392 C 820 440 560 432 400 380 C 370 300 350 150 340 0 Z" fill="url(#teamPhoto)"/>
    <path class="header-edge" d="M290 350 C 470 430 780 448 1030 392" fill="none" stroke="url(#spectrum)" stroke-width="6"/>

    <!-- copier -->
    <rect role="img" aria-label="Photo of a refurbished office multifunction copier"
          x="40" y="430" width="395" height="555" rx="6" fill="url(#copierPhoto)"/>

    <!-- footer -->
    <rect class="footer-bar" x="0" y="1138" width="1030" height="62" fill="var(--charcoal)"/>
    <path class="cta-panel" d="M600 1122 H1030 V1200 H578 Z" fill="var(--teal)"/>
  </svg>

  <h1 class="brand-name">Ribbon Works</h1>

  <section class="intro">
    <h2 class="intro-title">Rent, Lease, and Sell Refurbished Copiers!</h2>
    <p class="intro-text">We offer a two hour response time on all repairs within the DFW Metroplex. Our technicians have a minimum of 10 years repair experience and a combined total of 79 years! We offer the finest in state of the art equipment from manufacturers such as Norvale, Kestrel, and Halden Imaging.</p>
  </section>

  <section class="offer">
    <p class="offer-headline">Save up to 60% <span class="offer-off">off</span></p>
    <p class="offer-sub">Copy and printing costs</p>
  </section>

  <ul class="benefits">
    <li class="benefit"><svg viewBox="0 0 20 20"><circle cx="10" cy="10" r="10" fill="#1aa3c4"/><path d="M5.5 10.2 L8.7 13.2 L14.5 7" fill="none" stroke="#fff" stroke-width="2.4" stroke-linecap="round" stroke-linejoin="round"/></svg>80+ point inspection of equipment</li>
    <li class="benefit"><svg viewBox="0 0 20 20"><circle cx="10" cy="10" r="10" fill="#1aa3c4"/><path d="M5.5 10.2 L8.7 13.2 L14.5 7" fill="none" stroke="#fff" stroke-width="2.4" stroke-linecap="round" stroke-linejoin="round"/></svg>Full teardown and rebuild of like new units</li>
    <li class="benefit"><svg viewBox="0 0 20 20"><circle cx="10" cy="10" r="10" fill="#1aa3c4"/><path d="M5.5 10.2 L8.7 13.2 L14.5 7" fill="none" stroke="#fff" stroke-width="2.4" stroke-linecap="round" stroke-linejoin="round"/></svg>Transparent pricing</li>
    <li class="benefit"><svg viewBox="0 0 20 20"><circle cx="10" cy="10" r="10" fill="#1aa3c4"/><path d="M5.5 10.2 L8.7 13.2 L14.5 7" fill="none" stroke="#fff" stroke-width="2.4" stroke-linecap="round" stroke-linejoin="round"/></svg>Lease options</li>
    <li class="benefit"><svg viewBox="0 0 20 20"><circle cx="10" cy="10" r="10" fill="#1aa3c4"/><path d="M5.5 10.2 L8.7 13.2 L14.5 7" fill="none" stroke="#fff" stroke-width="2.4" stroke-linecap="round" stroke-linejoin="round"/></svg>6 month warranty</li>
    <li class="benefit"><svg viewBox="0 0 20 20"><circle cx="10" cy="10" r="10" fill="#1aa3c4"/><path d="M5.5 10.2 L8.7 13.2 L14.5 7" fill="none" stroke="#fff" stroke-width="2.4" stroke-linecap="round" stroke-linejoin="round"/></svg>Comprehensive maintenance programs</li>
  </ul>

  <div class="badge">Helping<br>business owners<br>save money</div>

  <footer class="footer-contacts">
    <span class="contact">
      <svg viewBox="0 0 26 26"><circle cx="13" cy="13" r="13" fill="#1aa3c4"/><circle cx="13" cy="13" r="7" fill="none" stroke="#fff" stroke-width="1.6"/><ellipse cx="13" cy="13" rx="3" ry="7" fill="none" stroke="#fff" stroke-width="1.4"/><path d="M6 13 H20" stroke="#fff" stroke-width="1.4"/></svg>
      ribbonworksgrp.com
    </span>
    <span class="contact">
      <svg viewBox="0 0 26 26"><circle cx="13" cy="13" r="13" fill="#1aa3c4"/><rect x="6.5" y="8.5" width="13" height="9" rx="1" fill="none" stroke="#fff" stroke-width="1.6"/><path d="M6.8 9 L13 14 L19.2 9" fill="none" stroke="#fff" stroke-width="1.6"/></svg>
      info@ribbonworksgrp.com
    </span>
  </footer>

  <div class="cta">
    <span class="cta-label">Free Quote</span>
    <span class="cta-phone">
      <svg viewBox="0 0 22 28"><rect x="3" y="1.5" width="16" height="25" rx="3" fill="none" stroke="#fff" stroke-width="2.2"/><path d="M8 22.5 H14" stroke="#fff" stroke-width="2"/></svg>
      +1 555-014-2890
    </span>
  </div>
</main>
</body>
</html>
```